Quillon Maison Wood Fired Pizza business card design

I have a logo and need an eye catching design that will get me noticed.
My business is wood fired pizza. I want a bold design that will make our customers remember us and the food that we serve. Work with the colors of our logo and texts. Maybe add designs that lend to what or how pizza is made using our wood fired oven?

Target Market(s)

Foodies!

Contact Information for Business Card

Quillon Maison Wood Fired Pizza
Our slogan is Fast. Fresh. Handcrafted
Catering for all events

Requirements
Must have
• Dana Porrick
Telephone 570 555 0183
website www.getquillon.example
Facebook @getquillonpizza maybe use the facebook logo next to it
Instagram getquillonpizza maybe use the instagram logo next to it
Catering for all events
Nice to have
• Maybe pizza peels, pizza cutters? Wood? Fired wood? Using our flame in the background?
Please work with different colored text so each sentence stands out? A themed color for facebook?
Maybe work with the colors within our logo?
Please try to use the our quillon font, but not a must have.

```html
<!DOCTYPE html>
<html lang="en">
<head>
<meta charset="utf-8">
<title>Quillon Maison Wood Fired Pizza – Business Card</title>
<link href="https://fonts.googleapis.com/css2?family=Work+Sans:wght@400;500;600;800&display=swap" rel="stylesheet">
<style>
  :root {
    --canvas: #e9e6e2;
    --card-dark: #17181f;
    --card-light: #ffffff;
    --flame-red: #d3222a;
    --ember-orange: #e8961e;
    --ink: #3a3a3a;
    --ink-soft: #5b5b5b;
    --white: #ffffff;
  }
  * { box-sizing: border-box; margin: 0; padding: 0; }
  html, body { width: 1200px; height: 912px; overflow: hidden; }
  body {
    background: var(--canvas);
    font-family: "Work Sans", Arial, sans-serif;
    position: relative;
  }
  .card {
    position: absolute;
    left: 290px;
    width: 620px;
    height: 354px;
    border-radius: 22px;
    overflow: hidden;
  }
  .card--front { top: 76px; background: var(--card-dark); }
  .card--back { top: 482px; background: var(--card-light); }

  /* front */
  .brand-lockup {
    position: absolute;
    left: 0; right: 0; top: 92px;
    display: flex; flex-direction: column; align-items: center;
  }
  .brand-lockup__dot {
    width: 54px; height: 54px; border-radius: 50%;
    background: var(--flame-red);
    margin-bottom: 18px;
  }
  .brand-lockup__name {
    color: var(--white);
    font-weight: 800;
    font-size: 38px;
    letter-spacing: 4px;
    text-transform: uppercase;
  }
  .brand-lockup__rule {
    width: 250px; height: 2px;
    background: var(--ember-orange);
    margin-top: 12px;
  }
  .slogan {
    position: absolute;
    left: 0; right: 0; bottom: 30px;
    text-align: center;
    color: var(--white);
    font-size: 17px;
    font-weight: 500;
    letter-spacing: 0.5px;
  }

  /* back */
  .back-brand {
    position: absolute;
    left: 40px; top: 0; width: 250px; height: 100%;
    display: flex; align-items: center; justify-content: center;
    color: var(--flame-red);
    font-weight: 800;
    font-size: 44px;
    letter-spacing: 2px;
    text-transform: uppercase;
  }
  .divider {
    position: absolute;
    left: 322px; top: 78px;
    width: 2px; height: 196px;
    background: var(--flame-red);
  }
  .contact {
    position: absolute;
    left: 350px; top: 72px;
  }
  .contact__name {
    color: var(--flame-red);
    font-size: 26px;
    font-weight: 500;
    text-transform: uppercase;
    letter-spacing: 0.5px;
  }
  .contact__role {
    color: var(--ink-soft);
    font-size: 18px;
    margin: 2px 0 14px 14px;
  }
  .contact__list { list-style: none; }
  .contact__item {
    display: flex; align-items: center; gap: 8px;
    color: var(--ink);
    font-size: 18px;
    line-height: 27px;
    margin-left: 22px;
  }
  .contact__item--gap { margin-top: 10px; }
  .contact__icon { width: 12px; height: 12px; flex: none; }
  .contact__mark {
    width: 10px; height: 10px; flex: none;
    background: var(--flame-red);
    border-radius: 2px;
  }
</style>
</head>
<body>
  <section class="card card--front" aria-label="Card front">
    <div class="brand-lockup">
      <span class="brand-lockup__dot"></span>
      <span class="brand-lockup__name">Quillon Maison</span>
      <span class="brand-lockup__rule"></span>
    </div>
    <p class="slogan">FAST. FRESH. HANDCRAFTED CATERING FOR ALL EVENTS</p>
  </section>

  <section class="card card--back" aria-label="Card back">
    <div class="back-brand">Quillon</div>
    <div class="divider"></div>
    <div class="contact">
      <h1 class="contact__name">Dana Porrick</h1>
      <p class="contact__role">Founder</p>
      <ul class="contact__list">
        <li class="contact__item"><span class="contact__mark"></span>getquillonpizza</li>
        <li class="contact__item"><span class="contact__mark"></span>getquillonpizza</li>
        <li class="contact__item contact__item--gap">
          <svg class="contact__icon" viewBox="0 0 12 12" aria-hidden="true"><path d="M2.5 1 L4.5 1 L5.2 3.6 L4 4.6 Q5 7 7.4 8 L8.4 6.8 L11 7.5 L11 9.5 Q10.5 11 8.8 11 Q1 10 1 2.8 Q1 1 2.5 1Z" fill="var(--flame-red)"/></svg>
          570 555 0183
        </li>
        <li class="contact__item">
          <svg class="contact__icon" viewBox="0 0 12 12" aria-hidden="true"><rect x="1" y="2.5" width="10" height="7" rx="1" fill="none" stroke="var(--flame-red)" stroke-width="1.4"/><path d="M1.5 3 L6 6.5 L10.5 3" fill="none" stroke="var(--flame-red)" stroke-width="1.4"/></svg>
          info@getquillon.example
        </li>
        <li class="contact__item">
          <svg class="contact__icon" viewBox="0 0 12 12" aria-hidden="true"><circle cx="6" cy="6" r="4.8" fill="none" stroke="var(--flame-red)" stroke-width="1.2"/><ellipse cx="6" cy="6" rx="2" ry="4.8" fill="none" stroke="var(--flame-red)" stroke-width="1"/><path d="M1.2 6 H10.8" stroke="var(--flame-red)" stroke-width="1"/></svg>
          www.getquillon.example
        </li>
      </ul>
    </div>
  </section>
</body>
</html>
```